International Life Insurer Needs a Web Design

What We Do: We are a boutique financial services firm specializing in solutions that financial services professionals can integrate into comprehensive wealth preservation strategies for their clients. Strategies we provide may run the spectrum from simple life insurance products to complex cases with very sophisticated and intricate solutions.

Industry Type: Financial & Insurance

Top Things to Communicate Through Our Web Design:
#1 Ultra High Net Worth
#2 INTERNATIONAL
#3 Private Banking
#4 Expertise
________________________________________
Our Target Audience:
Financial institutions/private banks who have high net worth/ultra high net worth international clients looking for unparalleled expertise in wealth preservation, taxation, and business insurance. The audience is the financial service professional, not the end client of the financial services. We will direct the professional to the site.
We Like These Designs. (fonts, colors, style):
Simple font, clean, modern, contemporary, blue colors
NOT stodgy, old, gothic, etc.

Secondarily, we’d like to also create a small tri-fold brochure incorporating the web elements (design, text), so the ability to transfer the design to print might be a plus.

Project Deadline Extended
Reason: to allow for additional design work

Target Market(s)

Financial services professionals catering to their ultra high net worth clients

Industry/Entity Type

Life Insurance

Requirements
Must have
• Our logo (see uploaded file)
Nice to have
• the existing website includes some text that could be reviewed for ideas and incorporated into the design: http://marlowcrestadvisory.example/

```html
<!DOCTYPE html>
<html lang="en">
<head>
<meta charset="utf-8">
<title>Marlowcrest Insurance Group – Web Design</title>
<link rel="stylesheet" href="https://fonts.googleapis.com/css2?family=Roboto:wght@300;400;500&display=swap">
<style>
  :root {
    --page-bg: #ffffff;
    --brand-navy: #1f4f8a;
    --band-navy: #023a79;
    --footer-navy: #032a59;
    --panel-blue: #0b66c4;
    --nav-blue: #0d66c4;
    --scroll-dark: #0a3566;
    --text-white: #ffffff;
    --menu-text: #0b5db5;
    --photo-light: #f4f5f6;
    --photo-mid: #d9dde2;
    --photo-dark: #9ea6b1;
  }
  * { box-sizing: border-box; margin: 0; padding: 0; }
  html, body { width: 1200px; height: 800px; overflow: hidden; background: var(--page-bg); }
  body { position: relative; font-family: "Roboto", Arial, sans-serif; }

  .screen {
    position: absolute;
    width: 855px;
    height: 683px;
    background: var(--page-bg);
    transform-origin: 0 0;
  }
  .screen--main { left: 22px; top: 62px; }
  .screen--preview-hnw { left: 897px; top: 60px; transform: scale(0.3263); }
  .screen--preview-nra { left: 897px; top: 292px; transform: scale(0.3263); }

  .brand { position: absolute; left: 32px; top: 24px; display: flex; align-items: center; gap: 12px; }
  .brand__square { width: 44px; height: 44px; background: var(--brand-navy); }
  .brand__name { color: var(--brand-navy); font-size: 29px; font-weight: 400; line-height: 30px; letter-spacing: -0.5px; }

  .hero-photo {
    position: absolute; left: 413px; top: 0; width: 442px; height: 212px;
    background: linear-gradient(120deg, var(--photo-light) 0%, var(--photo-mid) 45%, var(--photo-light) 70%, var(--photo-dark) 100%);
  }

  .band { position: absolute; left: 0; top: 212px; width: 855px; height: 471px; background: var(--band-navy); }
  .band__footer { position: absolute; left: 0; bottom: 0; width: 100%; height: 55px; background: var(--footer-navy); }

  .nav { position: absolute; top: 221px; height: 41px; left: 0; width: 855px; }
  .nav__item {
    position: absolute; top: 0; height: 41px; background: var(--nav-blue);
    color: var(--text-white); font-size: 17px; font-weight: 400;
    display: flex; align-items: center; justify-content: center;
  }
  .nav__item--home { left: 32px; width: 134px; font-weight: 500; }
  .nav__item--about { left: 175px; width: 169px; }
  .nav__item--solutions { left: 352px; width: 294px; }
  .nav__item--cases { left: 655px; width: 166px; }

  .panel { position: absolute; left: 32px; top: 270px; width: 789px; height: 357px; background: var(--panel-blue); }

  .submenu { position: absolute; left: 352px; top: 270px; width: 294px; }
  .submenu__item {
    height: 22px; margin-bottom: 2px; background: var(--text-white);
    color: var(--menu-text); font-size: 13px; line-height: 22px; padding-left: 11px;
  }

  .content { position: absolute; left: 76px; top: 324px; width: 680px; color: var(--text-white); }
  .content__title { font-size: 20px; font-weight: 400; line-height: 24px; }
  .content__body { margin-top: 36px; font-size: 16px; font-weight: 300; line-height: 20px; }
  .content__body p + p { margin-top: 20px; }
  .content__list { margin-top: 18px; list-style: none; }
  .content__list li { position: relative; padding-left: 44px; }
  .content__list li::before { content: "•"; position: absolute; left: 20px; }

  .content--nra .content__list { margin-top: 30px; font-size: 14px; line-height: 16px; }
  .content--nra .content__list li { margin-bottom: 22px; padding-left: 26px; }
  .content--nra .content__list li::before { left: 8px; }

  .scrollbar { position: absolute; left: 796px; top: 381px; width: 12px; height: 222px; }
  .scrollbar__thumb { position: absolute; left: 0; top: 0; width: 12px; height: 72px; background: var(--scroll-dark); }
  .scrollbar__track { position: absolute; left: 4px; top: 72px; width: 4px; height: 150px; background: var(--text-white); }
</style>
</head>
<body>

<section class="screen screen--main">
  <div class="brand"><span class="brand__square"></span><span class="brand__name">Marlowcrest<br>Insurance Group</span></div>
  <div class="hero-photo" role="img" aria-label="Photo of business hands reviewing financial charts with a pen"></div>
  <div class="band"><div class="band__footer"></div></div>
  <nav class="nav">
    <span class="nav__item nav__item--home">Home</span>
    <span class="nav__item nav__item--about">About Us</span>
    <span class="nav__item nav__item--solutions">Solutions for Diverse Needs</span>
    <span class="nav__item nav__item--cases">Case Studies</span>
  </nav>
  <div class="panel"></div>
  <div class="submenu">
    <div class="submenu__item">Solutions for High Net Worth Individuals</div>
    <div class="submenu__item">Solutions for Non-U.S. Resident Clients (NRAs)</div>
  </div>
  <article class="content">
    <h1 class="content__title">Solutions for High Net Worth Individuals</h1>
    <div class="content__body">
      <p>Clients with significant assets typically have more complicated wealth transfer and wealth protection concerns. In some circumstances, insurance might be used to collateralize loans or provide economic security to the lender, the borrower, or the borrower’s family. In other cases, non-resident status may complicate the financial services required in order to minimize tax impacts or other potential circumstances.</p>
      <p>For example, these considerations may point to a need for sophisticated insurance solutions:</p>
    </div>
    <ul class="content__list">
      <li>Immigration to the U.S.</li>
      <li>Business partnerships</li>
      <li>Outstanding credit lines</li>
    </ul>
  </article>
  <div class="scrollbar"><span class="scrollbar__thumb"></span><span class="scrollbar__track"></span></div>
</section>

<section class="screen screen--preview-hnw">
  <div class="brand"><span class="brand__square"></span><span class="brand__name">Marlowcrest<br>Insurance Group</span></div>
  <div class="hero-photo" role="img" aria-label="Photo of business hands reviewing financial charts with a pen"></div>
  <div class="band"><div class="band__footer"></div></div>
  <nav class="nav">
    <span class="nav__item nav__item--home">Home</span>
    <span class="nav__item nav__item--about">About Us</span>
    <span class="nav__item nav__item--solutions">Solutions for Diverse Needs</span>
    <span class="nav__item nav__item--cases">Case Studies</span>
  </nav>
  <div class="panel"></div>
  <article class="content">
    <h2 class="content__title">Solutions for High Net Worth Individuals</h2>
    <div class="content__body">
      <p>Clients with significant assets typically have more complicated wealth transfer and wealth protection concerns. In some circumstances, insurance might be used to collateralize loans or provide economic security to the lender, the borrower, or the borrower’s family. In other cases, non-resident status may complicate the financial services required in order to minimize tax impacts or other potential circumstances.</p>
      <p>For example, these considerations may point to a need for sophisticated insurance solutions:</p>
    </div>
    <ul class="content__list">
      <li>Immigration to the U.S.</li>
      <li>Business partnerships</li>
      <li>Outstanding credit lines</li>
    </ul>
  </article>
  <div class="scrollbar"><span class="scrollbar__thumb"></span><span class="scrollbar__track"></span></div>
</section>

<section class="screen screen--preview-nra">
  <div class="brand"><span class="brand__square"></span><span class="brand__name">Marlowcrest<br>Insurance Group</span></div>
  <div class="hero-photo" role="img" aria-label="Photo of business hands reviewing financial charts with a pen"></div>
  <div class="band"><div class="band__footer"></div></div>
  <nav class="nav">
    <span class="nav__item nav__item--home">Home</span>
    <span class="nav__item nav__item--about">About Us</span>
    <span class="nav__item nav__item--solutions">Solutions for Diverse Needs</span>
    <span class="nav__item nav__item--cases">Case Studies</span>
  </nav>
  <div class="panel"></div>
  <article class="content content--nra">
    <h2 class="content__title">Solutions for Non-U.S. Resident Clients (NRAs)</h2>
    <ul class="content__list">
      <li>Pre-immigration planning for non-resident clients</li>
      <li>Multi-jurisdictional estate planning</li>
      <li>Private placement life insurance and deferred variable annuities for customizable insurance solutions that address complex needs, including tax efficient asset transfer or insurance as a complement to traditional fiduciary structures</li>
      <li>Non-U.S. resident clients with intended beneficiaries residing in the U.S.</li>
      <li>Clients with non-U.S. related planning needs</li>
    </ul>
  </article>
  <div class="scrollbar"><span class="scrollbar__thumb"></span><span class="scrollbar__track"></span></div>
</section>

</body>
</html>
```